Boot Camp Flyer

Outdoor Boot Camp
SAMPLE DESIGNS I LIKE UPLOADED.
Similar to this or be creative !
I need A5 and DL flyer promoting our Boot Camp program, similar to the sample design but include our details. Pink blue green black white yellow and purple colours ok

PRICE: $100
WHEN: Thursdays & Saturdays
Thursday 6pm
Saturday 9am

WHERE: Brindmoor Glen

Get results all year round! 5 week boot camp only $100
Join in any time! Register your place now!

Stride Forge Boot Camp
Register now at lumatrekgym@mailvera.com or www.socialpage-example.com/lumatrekgymnz
Female only. Registration essential. ALL fitness levels welcome.

Conditions
Valid from Mar 22, 2018
Expires 26th Apr, 2018
Register online. Subject to availability. Valid for new clients only. Valid for unlimited sessions per week. Boot Camps run in 5 week blocks. Non-transferable. No refunds unless required by law. No cashback. Not to be used with any other offer.

Could maybe write 5 week stride forge challenge

Target Market(s)

Female 20s-40s

Industry/Entity Type

Fitness

Colors

Requirements
Must have
• Colour
• Easy to read font
• Picture of females (target market) exercising
Nice to have
• Terms and conditions in small print down bottom.
Should not have
• Too much text

```html
<!DOCTYPE html>
<html lang="en">
<head>
<meta charset="utf-8">
<title>5 Week Stride Forge Challenge – Flyer</title>
<link rel="stylesheet" href="https://fonts.googleapis.com/css2?family=Raleway:wght@400;500;600;700;800;900&display=swap">
<style>
  :root {
    --purple: #8e2a8f;
    --purple-deep: #6f1f74;
    --yellow: #fff200;
    --gold: #f7e21b;
    --blue: #1f7fc4;
    --blush: #fbe9f3;
    --lavender: #f1eef6;
    --ink: #2a2a2a;
    --white: #ffffff;
    --stage: #e9e9e9;
  }
  * { box-sizing: border-box; margin: 0; padding: 0; }
  html, body {
    width: 1200px; height: 841px; overflow: hidden;
    background: var(--stage);
    font-family: "Raleway", Arial, sans-serif;
  }
  .flyer {
    position: absolute; left: 304px; top: 0;
    width: 592px; height: 841px;
    background: var(--white); overflow: hidden;
  }
  .edge-bar {
    position: absolute; left: 0; width: 100%; height: 17px;
    background: linear-gradient(90deg, var(--purple) 0%, #c33a9d 25%, var(--yellow) 50%, #8ccf6a 70%, var(--blue) 100%);
  }
  .edge-bar--top { top: 0; }
  .edge-bar--bottom { bottom: 0; height: 21px; }
  .hero-photo {
    position: absolute; left: 0; top: 20px; width: 100%; height: 384px;
    background: linear-gradient(100deg, #8a3a8e 0%, #a05a86 22%, #9c9a5c 45%, #d8d23a 58%, #5e9a6a 75%, #2f6f78 100%);
  }
  .headline {
    position: absolute; right: 14px; top: 236px;
    color: #fdf1f8; text-align: right; font-weight: 800;
    text-shadow: 2px 3px 3px rgba(0,0,0,.55); line-height: .95;
  }
  .headline__top { display: flex; align-items: center; justify-content: flex-end; gap: 10px; }
  .headline__num { font-size: 86px; font-weight: 900; line-height: .85; }
  .headline__stack { display: flex; flex-direction: column; align-items: flex-end; }
  .headline__week { font-size: 46px; }
  .headline__mid { font-size: 31px; }
  .headline__end { font-size: 40px; margin-top: 2px; }
  .info-band {
    position: absolute; left: 0; top: 406px; width: 100%; height: 88px;
    background: var(--purple); color: var(--white);
    padding-left: 198px; text-align: center;
    font-weight: 700; font-size: 14px; line-height: 1.5;
    display: flex; flex-direction: column; justify-content: center;
  }
  .info-band .label, .info-band .accent { color: var(--gold); }
  .info-band .price { font-size: 17px; }
  .where-band {
    position: absolute; left: 0; top: 494px; width: 100%; height: 28px;
    background: var(--blush); padding-left: 198px; text-align: center;
    font-weight: 700; font-size: 16px; line-height: 28px; color: var(--purple);
  }
  .where-band .place { color: var(--blue); }
  .promo-band {
    position: absolute; left: 0; top: 522px; width: 100%; height: 85px;
    background: var(--yellow);
  }
  .promo-band__pitch {
    position: absolute; left: 198px; right: 0; top: 8px;
    text-align: center; font-weight: 700; font-size: 14px; line-height: 1.3; color: var(--ink);
  }
  .promo-band__cta {
    position: absolute; left: 16px; top: 52px;
    font-weight: 800; font-size: 14.5px; color: var(--ink); white-space: nowrap;
  }
  .promo-band__cta span { color: var(--purple); }
  .brand-panel {
    position: absolute; left: -6px; top: 365px; width: 204px; height: 196px;
    background: var(--blush); border: 4px solid var(--purple);
    border-radius: 0 95px 95px 0;
    display: flex; align-items: center; justify-content: center; gap: 8px;
  }
  .brand-panel__dot { width: 14px; height: 14px; border-radius: 50%; background: var(--purple); }
  .brand-panel__name { font-weight: 800; font-size: 19px; color: var(--purple-deep); }
  .details {
    position: absolute; left: 0; top: 607px; width: 100%; height: 213px;
    background: var(--lavender);
  }
  .details__copy {
    position: absolute; left: 16px; top: 26px; width: 302px;
    font-size: 9.6px; line-height: 1.45; color: #333;
  }
  .details__title { font-weight: 700; font-size: 12.5px; color: var(--purple); margin-bottom: 2px; }
  .details__block + .details__block { margin-top: 12px; }
  .details__dates { font-weight: 700; }
  .details__terms { text-align: justify; }
  .class-photo {
    position: absolute; left: 322px; top: 600px; width: 274px; height: 222px;
    border-top: 4px solid var(--blue); border-left: 4px solid var(--blue);
    border-top-left-radius: 40px;
    background: linear-gradient(180deg, #b8cbdc 0%, #7e9d6e 35%, #b08a63 60%, #c9a783 100%);
  }
  .female-badge {
    position: absolute; left: 282px; top: 618px; width: 88px; height: 88px;
    border-radius: 50%; background: var(--purple); border: 4px solid var(--yellow);
    box-shadow: 0 0 0 3px var(--purple);
    display: flex; align-items: center; justify-content: center; text-align: center;
    color: var(--yellow); font-weight: 800; font-size: 15px; line-height: 1.05;
    transform: rotate(-14deg);
  }
</style>
</head>
<body>
  <main class="flyer">
    <div class="edge-bar edge-bar--top"></div>

    <div class="hero-photo" role="img" aria-label="Photo of women doing push-ups outdoors on grass while a trainer stands watching, tinted purple, yellow and teal"></div>

    <h1 class="headline">
      <div class="headline__top">
        <span class="headline__num">5</span>
        <span class="headline__stack">
          <span class="headline__week">WEEK</span>
          <span class="headline__mid">STRIDE FORGE</span>
        </span>
      </div>
      <div class="headline__end">CHALLENGE</div>
    </h1>

    <section class="info-band">
      <p><span class="label">PRICE:</span> <span class="price">$100</span></p>
      <p><span class="label">WHEN:</span> Thursdays &amp; Saturdays <span class="accent">22nd</span> March - <span class="accent">26th</span> April</p>
      <p>Thursday <span class="accent">6pm</span> &nbsp;|&nbsp; Saturday <span class="accent">9am</span></p>
    </section>

    <p class="where-band">WHERE: <span class="place">Brindmoor Glen</span></p>

    <section class="promo-band">
      <p class="promo-band__pitch">Get results all year round!<br>5 week boot camp only $100.</p>
      <p class="promo-band__cta">Join in any time! <span>REGISTER YOUR PLACE NOW!</span></p>
    </section>

    <div class="brand-panel">
      <span class="brand-panel__dot"></span>
      <span class="brand-panel__name">Lumatrek Gym</span>
    </div>

    <section class="details">
      <div class="details__copy">
        <div class="details__block">
          <h2 class="details__title">Stride Forge Boot Camp</h2>
          <p>Register now at lumatrekgym@mailvera.com<br>or www.socialpage-example.com/lumatrekgymnz<br>Registeration essential. ALL fitness levels welcome.</p>
        </div>
        <div class="details__block">
          <h2 class="details__title">Conditions</h2>
          <p class="details__dates">Valid from Mar 22, 2018<br>Expires 26th Apr, 2018</p>
          <p class="details__terms">Register online. Subject to availability. Valid for new clients only. Valid for unlimited sessions per week. Blocks start on 22nd March 2018. Non-transferable. No refunds unless required by law. No cashback. Not to be used with any other offer.</p>
        </div>
      </div>
    </section>

    <div class="class-photo" role="img" aria-label="Photo of a women's outdoor group fitness class stretching arms overhead on a wooden deck"></div>

    <div class="female-badge">FEMALE<br>ONLY</div>

    <div class="edge-bar edge-bar--bottom"></div>
  </main>
</body>
</html>
```